Kestrel Gardenworks Business Card

An eye catching, yet simple business card that includes;

1. our logo
2. office phone - 5083172946
3. email - kestrelgardenworks@mailbrook.com
4. website - www.kestrelgardenworks.com
5. instagram - @kestrelgardenworksnv

```html
<!DOCTYPE html>
<html lang="en">
<head>
<meta charset="utf-8">
<title>Kestrel Gardenworks Business Card</title>
<link rel="stylesheet" href="https://fonts.googleapis.com/css2?family=Montserrat:wght@500;700&family=Open+Sans:wght@400&display=swap">
<style>
  :root {
    --stage: #2b2b2b;
    --card-dark: #1e1816;
    --bronze: #a3612a;
    --paper: #ffffff;
    --ink-light: #f4f1ee;
  }
  * { margin: 0; padding: 0; box-sizing: border-box; }
  html, body { width: 1200px; height: 1015px; overflow: hidden; }
  body {
    background: var(--stage);
    position: relative;
    font-family: "Open Sans", sans-serif;
  }
  .card {
    position: absolute;
    width: 640px;
    height: 366px;
    background: var(--card-dark);
    overflow: hidden;
    box-shadow: 0 14px 30px rgba(0,0,0,0.45);
  }
  .card--back { left: 110px; top: 80px; }
  .card--front { left: 450px; top: 560px; }

  .brand {
    font-family: "Montserrat", sans-serif;
    font-weight: 700;
    color: var(--bronze);
    display: flex;
    align-items: center;
    gap: 12px;
    white-space: nowrap;
  }
  .brand__dot {
    width: 18px; height: 18px; border-radius: 50%;
    background: var(--bronze);
    flex: none;
  }
  .card--back .brand {
    position: absolute;
    left: 50%; top: 50%;
    transform: translate(-50%, -50%);
    font-size: 34px;
  }

  .front__disc {
    position: absolute;
    left: 0; top: 0;
    width: 640px; height: 366px;
  }
  .card--front .brand {
    position: absolute;
    left: 372px; top: 136px;
    width: 252px;
    font-size: 19px;
    color: var(--card-dark);
    justify-content: center;
    gap: 10px;
  }
  .card--front .brand .brand__dot { width: 14px; height: 14px; }

  .person {
    position: absolute;
    left: 48px; top: 58px;
  }
  .person__name {
    font-family: "Montserrat", sans-serif;
    font-weight: 700;
    font-size: 27px;
    color: var(--bronze);
    line-height: 1.1;
  }
  .person__title {
    font-family: "Montserrat", sans-serif;
    font-weight: 500;
    font-size: 15px;
    color: var(--ink-light);
    margin-top: 2px;
  }

  .contacts {
    position: absolute;
    left: 48px; bottom: 34px;
    list-style: none;
  }
  .contacts__item {
    display: flex;
    align-items: center;
    gap: 10px;
    font-size: 14px;
    color: var(--ink-light);
    line-height: 24px;
    white-space: nowrap;
  }
  .contacts__icon { width: 16px; height: 16px; flex: none; }
</style>
</head>
<body>

  <section class="card card--back" aria-label="Card back">
    <div class="brand"><span class="brand__dot"></span>Kestrel Gardenworks</div>
  </section>

  <section class="card card--front" aria-label="Card front">
    <svg class="front__disc" viewBox="0 0 640 366" aria-hidden="true">
      <circle cx="508" cy="154" r="200" fill="none" stroke="#a3612a" stroke-width="5"/>
      <circle cx="520" cy="150" r="200" fill="#ffffff"/>
    </svg>

    <div class="brand"><span class="brand__dot"></span>Kestrel Gardenworks</div>

    <div class="person">
      <p class="person__name">Daniel Hartley</p>
      <p class="person__title">Managing Director</p>
    </div>

    <ul class="contacts">
      <li class="contacts__item">
        <svg class="contacts__icon" viewBox="0 0 16 16" aria-hidden="true"><path d="M3.5 1.5l2.5 0 1 3.5-1.7 1.2a8 8 0 0 0 4.5 4.5L11 9l3.5 1v2.5c0 1-1 2-2 2A11 11 0 0 1 1.5 3.5c0-1 1-2 2-2z" fill="#a3612a"/></svg>
        5083172946
      </li>
      <li class="contacts__item">
        <svg class="contacts__icon" viewBox="0 0 16 16" aria-hidden="true"><rect x="1" y="3" width="14" height="10" fill="#a3612a"/><path d="M1 3l7 6 7-6" fill="none" stroke="#1e1816" stroke-width="1.3"/></svg>
        kestrelgardenworks@mailbrook.com
      </li>
      <li class="contacts__item">
        <svg class="contacts__icon" viewBox="0 0 16 16" aria-hidden="true"><g fill="none" stroke="#a3612a" stroke-width="1.4"><circle cx="8" cy="8" r="6.5"/><ellipse cx="8" cy="8" rx="3" ry="6.5"/><path d="M1.5 8h13M2.5 4.8h11M2.5 11.2h11"/></g></svg>
        www.kestrelgardenworks.com
      </li>
      <li class="contacts__item">
        <svg class="contacts__icon" viewBox="0 0 16 16" aria-hidden="true"><rect x="1.5" y="1.5" width="13" height="13" rx="3" fill="none" stroke="#a3612a" stroke-width="1.6"/></svg>
        @kestrelgardenworksnv
      </li>
    </ul>
  </section>

</body>
</html>
```